Software - upgrade look and feel

Brightmile Ledgerworks is the worldwide distributor of the uPlotta software application, which powers a loan strategy as described at www.brightmileledgerworks.com.The company has recently upgraded its image and website; and now seeks to give uPlotta a much-needed face-lift.Using the screen shots of the existing application (2 x screens provided), recreate the screens in a modern and vibrant style that generates a feeling of professionalism and confidence.
Updates

Project not yet launched and I felt 5 days was inadequate.

Target Market(s)

Financial services industry and their clients.

Industry/Entity Type

Financial Service

Font styles to use
Other font styles liked:
• See our website at brightmileledgerworks.com - happy with this font, but open to ideas.

Colors

Designer to choose colors to be used in the design.

Requirements
Must have
• Existing fields, but perhaps more intuitive for the User.
Nice to have
• A less busy look that suggests an innovative software application.
Should not have
• Complication.

```html
<!DOCTYPE html>
<html lang="en">
<head>
<meta charset="utf-8">
<title>uPlotta – Results</title>
<link href="https://fonts.googleapis.com/css2?family=Oswald:wght@300;400;500&family=Open+Sans:wght@400;600;700&display=swap" rel="stylesheet">
<style>
:root{
  --navy:#0b5f87;
  --navy-dark:#0a5a80;
  --tab:#1d84a8;
  --green:#7cc242;
  --page:#f6f7f8;
  --card:#ffffff;
  --line:#e6e9ec;
  --panel:#eaf2f5;
  --field:#d9e8ef;
  --sky:#2fa4ee;
  --amber:#fbb416;
  --red:#e6202b;
  --ink:#333333;
  --muted:#888888;
  --tip:#666666;
}
*{margin:0;padding:0;box-sizing:border-box}
html,body{width:1200px;height:932px;overflow:hidden;background:var(--page)}
.stage{position:absolute;left:0;top:0;width:1366px;height:1061px;transform:scale(0.87848);transform-origin:0 0;font-family:"Open Sans",sans-serif;color:var(--ink)}
.abs{position:absolute}
.topbar{left:0;top:0;width:1366px;height:48px;background:var(--navy)}
.brand{left:24px;top:9px;display:flex;align-items:center;gap:8px;color:#fff;font-family:"Oswald",sans-serif;font-weight:400;font-size:24px;line-height:30px}
.brand-mark{width:28px;height:28px;background:#fff;border-radius:3px}
.menu{left:155px;top:0;display:flex;height:48px}
.menu a{display:flex;align-items:center;justify-content:center;color:#fff;text-decoration:none;font-weight:700;font-size:11px;letter-spacing:.3px;border-right:1px solid rgba(0,0,0,.15)}
.menu a.active{background:var(--tab);width:120px}
.menu a.item{width:92px}
.user{right:24px;top:0;height:48px;display:flex;align-items:center;gap:8px;color:#fff;font-weight:700;font-size:11px}
.steps-label{top:141px;font-family:"Oswald",sans-serif;font-weight:300;font-size:14px;color:#444;text-align:center;width:160px;margin-left:-80px}
.steps-label.current{color:var(--navy)}
.card{left:48px;top:228px;width:980px;height:702px;background:var(--card);border:1px solid var(--line)}
.panel{left:1027px;top:228px;width:290px;height:702px;background:var(--panel)}
.results-title{left:73px;top:268px;font-family:"Oswald",sans-serif;color:var(--navy);font-size:28px;font-weight:500;line-height:38px}
.results-title span{font-weight:300;font-size:23px}
.select{left:73px;top:330px;width:480px;height:48px;border:1px solid #bdbdbd;display:flex;align-items:center;justify-content:space-between;padding:0 16px;font-weight:600;font-size:15px;letter-spacing:.2px;color:#333}
.info{left:561px;top:346px}
.btn{top:833px;width:160px;height:48px;border-radius:24px;display:flex;align-items:center;justify-content:center;font-family:"Oswald",sans-serif;font-size:18px;font-weight:400}
.btn-report{left:73px;background:var(--navy-dark);color:#fff}
.btn-save{left:241px;background:var(--sky);color:#fff}
.btn-cancel{left:409px;border:1px solid var(--sky);color:var(--sky);font-weight:300;background:#fff}
.savings-title{left:1052px;top:268px;font-family:"Oswald",sans-serif;color:var(--navy);font-size:28px;font-weight:500;line-height:38px}
.field-label{left:1052px;font-family:"Oswald",sans-serif;font-weight:400;font-size:14px;color:#444;display:flex;align-items:center;gap:4px}
.field{left:1052px;width:240px;height:40px;background:var(--field);color:var(--navy);font-weight:600;font-size:16px;padding-left:12px;display:flex;align-items:center}
.footer{left:0;width:1366px;top:1022px;text-align:center;font-size:11px;color:#888}
.footer span{margin:0 8px}
.chart text{font-family:"Oswald",sans-serif;font-weight:300;fill:#333}
</style>
</head>
<body>
<div class="stage">
  <header class="abs topbar"></header>
  <div class="abs brand"><span class="brand-mark"></span>uPlotta</div>
  <nav class="abs menu">
    <a class="active" href="#">CALCULATER</a>
    <a class="item" href="#">MENU 2</a>
    <a class="item" href="#">MENU 3</a>
  </nav>
  <div class="abs user">Username
    <svg width="12" height="8" viewBox="0 0 12 8"><path d="M1 1l5 5 5-5" stroke="#fff" stroke-width="2" fill="none"/></svg>
  </div>

  <div class="abs steps-label" style="left:443px">CLIENT / INCOME</div>
  <div class="abs steps-label" style="left:563px">EXPENSES</div>
  <div class="abs steps-label" style="left:683px">ASSETS / LIABILITIES</div>
  <div class="abs steps-label" style="left:803px">RESTRUCTURE</div>
  <div class="abs steps-label current" style="left:923px">CALCULATE</div>
  <svg class="abs" style="left:400px;top:160px" width="560" height="50" viewBox="400 160 560 50">
    <line x1="443" y1="183" x2="895" y2="183" stroke="var(--green)" stroke-width="3"/>
    <line x1="875" y1="183" x2="923" y2="183" stroke="var(--navy)" stroke-width="3"/>
    <g fill="var(--green)">
      <circle cx="443" cy="183" r="20"/><circle cx="563" cy="183" r="20"/><circle cx="683" cy="183" r="20"/><circle cx="803" cy="183" r="20"/>
    </g>
    <g stroke="#fff" stroke-width="3.5" fill="none" stroke-linecap="round" stroke-linejoin="round">
      <path d="M435 183l6 6 10-11"/><path d="M555 183l6 6 10-11"/><path d="M675 183l6 6 10-11"/><path d="M795 183l6 6 10-11"/>
    </g>
    <circle cx="923" cy="183" r="20" fill="var(--navy)"/>
    <text x="923" y="190" text-anchor="middle" font-family="Oswald, sans-serif" font-size="18" fill="#fff">5</text>
  </svg>

  <section class="abs card"></section>
  <aside class="abs panel"></aside>
  <svg class="abs" style="left:1027px;top:268px" width="14" height="38" viewBox="0 0 14 38"><path d="M0 0l14 19L0 38z" fill="#fff"/></svg>

  <h1 class="abs results-title">RESULTS <span>(for Liam &amp; Nora Penfold)</span></h1>
  <div class="abs select">GRAPH - YEARS/INTEREST SAVED
    <svg width="16" height="10" viewBox="0 0 16 10"><path d="M1 1l7 7 7-7" stroke="#888" stroke-width="1.6" fill="none"/></svg>
  </div>
  <svg class="abs info" width="17" height="17" viewBox="0 0 17 17"><circle cx="8.5" cy="8.5" r="7.5" fill="none" stroke="var(--green)" stroke-width="1.3"/><rect x="7.8" y="7" width="1.4" height="5.5" fill="var(--green)"/><rect x="7.8" y="4.2" width="1.4" height="1.6" fill="var(--green)"/></svg>

  <svg class="abs chart" style="left:80px;top:395px" width="930" height="415" viewBox="80 395 930 415">
    <g stroke="#eeeeee" stroke-width="1">
      <line x1="138" y1="442" x2="1000" y2="442"/><line x1="138" y1="474" x2="1000" y2="474"/><line x1="138" y1="506" x2="1000" y2="506"/><line x1="138" y1="538" x2="1000" y2="538"/><line x1="138" y1="570" x2="1000" y2="570"/><line x1="138" y1="602" x2="1000" y2="602"/><line x1="138" y1="634" x2="1000" y2="634"/><line x1="138" y1="666" x2="1000" y2="666"/><line x1="138" y1="698" x2="1000" y2="698"/><line x1="138" y1="730" x2="1000" y2="730"/>
      <line x1="167" y1="402" x2="167" y2="762"/><line x1="196" y1="402" x2="196" y2="762"/><line x1="225" y1="402" x2="225" y2="762"/><line x1="254" y1="402" x2="254" y2="762"/><line x1="283" y1="402" x2="283" y2="762"/><line x1="311" y1="402" x2="311" y2="762"/><line x1="340" y1="402" x2="340" y2="762"/><line x1="369" y1="402" x2="369" y2="762"/><line x1="398" y1="402" x2="398" y2="762"/><line x1="427" y1="402" x2="427" y2="762"/><line x1="455" y1="402" x2="455" y2="762"/><line x1="484" y1="402" x2="484" y2="762"/><line x1="513" y1="402" x2="513" y2="762"/><line x1="542" y1="402" x2="542" y2="762"/><line x1="571" y1="402" x2="571" y2="762"/><line x1="599" y1="402" x2="599" y2="762"/><line x1="628" y1="402" x2="628" y2="762"/><line x1="657" y1="402" x2="657" y2="762"/><line x1="686" y1="402" x2="686" y2="762"/><line x1="714" y1="402" x2="714" y2="762"/><line x1="743" y1="402" x2="743" y2="762"/><line x1="772" y1="402" x2="772" y2="762"/><line x1="801" y1="402" x2="801" y2="762"/><line x1="830" y1="402" x2="830" y2="762"/><line x1="858" y1="402" x2="858" y2="762"/><line x1="887" y1="402" x2="887" y2="762"/><line x1="916" y1="402" x2="916" y2="762"/><line x1="945" y1="402" x2="945" y2="762"/><line x1="974" y1="402" x2="974" y2="762"/>
    </g>
    <line x1="138" y1="402" x2="138" y2="762" stroke="#333"/>
    <line x1="138" y1="762" x2="1002" y2="762" stroke="#333"/>
    <text x="133" y="413" text-anchor="end" font-size="13" font-weight="400">BALANCE</text>
    <g font-size="11" text-anchor="end">
      <text x="133" y="446">500,000</text><text x="133" y="478">450,000</text><text x="133" y="510">400,000</text><text x="133" y="542">350,000</text><text x="133" y="574">300,000</text><text x="133" y="606">250,000</text><text x="133" y="638">200,000</text><text x="133" y="670">150,000</text><text x="133" y="702">100,000</text><text x="133" y="734">50,000</text>
    </g>
    <g fill="var(--amber)">
      <rect x="147" y="418" width="6" height="344"/><rect x="176" y="422" width="6" height="340"/><rect x="205" y="426" width="6" height="336"/><rect x="233" y="434" width="6" height="328"/><rect x="262" y="442" width="6" height="320"/><rect x="291" y="450" width="6" height="312"/><rect x="320" y="458" width="6" height="304"/><rect x="349" y="466" width="6" height="296"/><rect x="377" y="474" width="6" height="288"/><rect x="406" y="482" width="6" height="280"/><rect x="435" y="490" width="6" height="272"/><rect x="464" y="498" width="6" height="264"/><rect x="493" y="506" width="6" height="256"/><rect x="521" y="514" width="6" height="248"/><rect x="550" y="522" width="6" height="240"/><rect x="579" y="530" width="6" height="232"/><rect x="608" y="546" width="6" height="216"/><rect x="636" y="554" width="6" height="208"/><rect x="665" y="570" width="6" height="192"/><rect x="694" y="578" width="6" height="184"/><rect x="723" y="594" width="6" height="168"/><rect x="752" y="602" width="6" height="160"/><rect x="780" y="618" width="6" height="144"/><rect x="809" y="634" width="6" height="128"/><rect x="838" y="642" width="6" height="120"/><rect x="867" y="658" width="6" height="104"/><rect x="896" y="674" width="6" height="88"/><rect x="924" y="698" width="6" height="64"/><rect x="953" y="714" width="6" height="48"/>
    </g>
    <g fill="var(--red)">
      <rect x="153" y="426" width="6" height="336"/><rect x="182" y="430" width="6" height="332"/><rect x="211" y="434" width="6" height="328"/><rect x="239" y="442" width="6" height="320"/><rect x="268" y="458" width="6" height="304"/><rect x="297" y="466" width="6" height="296"/><rect x="326" y="482" width="6" height="280"/><rect x="355" y="498" width="6" height="264"/><rect x="383" y="506" width="6" height="256"/><rect x="412" y="522" width="6" height="240"/><rect x="441" y="530" width="6" height="232"/><rect x="470" y="546" width="6" height="216"/><rect x="499" y="562" width="6" height="200"/><rect x="527" y="578" width="6" height="184"/><rect x="556" y="594" width="6" height="168"/><rect x="585" y="610" width="6" height="152"/><rect x="614" y="626" width="6" height="136"/><rect x="642" y="642" width="6" height="120"/><rect x="671" y="658" width="6" height="104"/><rect x="700" y="682" width="6" height="80"/><rect x="729" y="706" width="6" height="56"/><rect x="758" y="722" width="6" height="40"/>
    </g>
    <g font-size="12" text-anchor="middle">
      <text x="153" y="781">1</text><text x="182" y="781">2</text><text x="211" y="781">3</text><text x="239" y="781">4</text><text x="268" y="781">5</text><text x="297" y="781">6</text><text x="326" y="781">7</text><text x="355" y="781">8</text><text x="383" y="781">9</text><text x="412" y="781">10</text><text x="441" y="781">11</text><text x="470" y="781">12</text><text x="499" y="781">13</text><text x="527" y="781">14</text><text x="556" y="781">15</text><text x="585" y="781">16</text><text x="614" y="781">17</text><text x="642" y="781">18</text><text x="671" y="781">19</text><text x="700" y="781">20</text><text x="729" y="781">21</text><text x="758" y="781">22</text><text x="786" y="781">23</text><text x="815" y="781">24</text><text x="844" y="781">25</text><text x="873" y="781">26</text><text x="902" y="781">27</text><text x="930" y="781">28</text><text x="959" y="781">29</text><text x="988" y="781">30</text>
    </g>
    <text x="569" y="800" text-anchor="middle" font-size="13">TERM (Yrs)</text>

    <rect x="879.5" y="418.5" width="107" height="64" fill="#fff" stroke="#eeeeee"/>
    <rect x="896" y="434" width="11" height="11" fill="var(--amber)"/>
    <rect x="896" y="454" width="11" height="11" fill="var(--red)"/>
    <text x="912" y="444" font-family="Open Sans, sans-serif" font-size="11" style="font-family:'Open Sans',sans-serif;font-weight:400">Data Label</text>
    <text x="912" y="464" font-size="11" style="font-family:'Open Sans',sans-serif;font-weight:400">Data Label</text>

    <rect x="713" y="451" width="90" height="127" rx="3" fill="var(--tip)"/>
    <path d="M750 578h16l-8 14z" fill="var(--tip)"/>
    <text x="758" y="480" text-anchor="middle" font-size="17" style="fill:#fff">TERM 22</text>
    <line x1="738" y1="489" x2="778" y2="489" stroke="#fff"/>
    <g text-anchor="middle" style="font-family:'Open Sans',sans-serif">
      <text x="758" y="510" font-size="11" style="fill:#fff;font-family:'Open Sans',sans-serif;font-weight:600">Data Lable</text>
      <text x="758" y="527" font-size="12" style="fill:#fff;font-family:'Open Sans',sans-serif;font-weight:700">$250,000</text>
      <text x="758" y="549" font-size="11" style="fill:#fff;font-family:'Open Sans',sans-serif;font-weight:600">Data Lable</text>
      <text x="758" y="566" font-size="12" style="fill:#fff;font-family:'Open Sans',sans-serif;font-weight:700">$60,000</text>
    </g>
  </svg>

  <a class="abs btn btn-report">REPORT</a>
  <a class="abs btn btn-save">SAVE</a>
  <a class="abs btn btn-cancel">CANCEL</a>

  <h2 class="abs savings-title">SAVINGS</h2>
  <div class="abs field-label" style="top:326px">Potential Years Saved
    <svg width="16" height="16" viewBox="0 0 17 17"><circle cx="8.5" cy="8.5" r="7.5" fill="none" stroke="var(--green)" stroke-width="1.3"/><rect x="7.8" y="7" width="1.4" height="5.5" fill="var(--green)"/><rect x="7.8" y="4.2" width="1.4" height="1.6" fill="var(--green)"/></svg>
  </div>
  <div class="abs field" style="top:350px">7.00</div>
  <div class="abs field-label" style="top:410px">Potential Interesrt Saved
    <svg width="16" height="16" viewBox="0 0 17 17"><circle cx="8.5" cy="8.5" r="7.5" fill="none" stroke="var(--green)" stroke-width="1.3"/><rect x="7.8" y="7" width="1.4" height="5.5" fill="var(--green)"/><rect x="7.8" y="4.2" width="1.4" height="1.6" fill="var(--green)"/></svg>
  </div>
  <div class="abs field" style="top:434px">$105,336.33</div>
  <div class="abs field-label" style="top:494px">Extra Payment Savings</div>
  <div class="abs field" style="top:518px">$101,629.50</div>
  <div class="abs field-label" style="top:578px">Offset Savings</div>
  <div class="abs field" style="top:602px">$3,706.83</div>

  <footer class="abs footer">©2019 Brightmile Ledgerworks Pty Ltd<span>|</span>Contact<span>|</span>Legal Notice</footer>
</div>
</body>
</html>
```